User-interface and web design for new forum-style communication platform

We developed a new forum-style communication platform specially targetting stock investors to share and discuss information on companies listed on the stock exchange.

You have complete freedom for designing the user-interface and web design. Designs should include all features listed below.

Please read the attached document for full specifications. Also attached is a mockup of the layout, but this is only directional. A mockup for the user-profile is also attached, but does not need to be designed.

This project focusses on the homepage and thread view.

The winner(s) will be asked to design the complete project. (create thread box, user profile, registering, settings...)

We are looking for a well thought out, smart design that incorporates the specifications in the attached document. Please do not hesitate to contact us if anything is not clear.

Target Market(s)

Stock investors from 25 to 60 years old (the people that are currently on investor forums)

Industry/Entity Type

Communication

Font styles to use
Sans Serif

Colors

Designer to choose colors to be used in the design.

Requirements
Must have
• Full homepage design & Thread view specified in the attached document.
Nice to have
• Create thread view
- Field for adding tags
- field for subject of the thread
- text box with basic text editing
- method for sharing media
Should not have
• Logo design.

```html
<!DOCTYPE html>
<html lang="en">
<head>
<meta charset="utf-8">
<title>Public: Talvenix – Conversations</title>
<link href="https://fonts.googleapis.com/css2?family=Roboto:ital,wght@0,300;0,400;0,500;0,700;1,400;1,500&family=Roboto+Slab:wght@300;400&display=swap" rel="stylesheet">
<style>
:root{
  --navy:#06103f;
  --navy-text:#0b1446;
  --cyan:#1a9fc9;
  --cyan-btn:#1aa3cf;
  --page:#ececec;
  --white:#ffffff;
  --line:#d3d3d3;
  --body:#4a4a4a;
  --muted:#a8a8a8;
  --soft-blue:#dae4f2;
  --rail:#c9ced9;
  --stat:#f4f4f4;
}
*{box-sizing:border-box;margin:0;padding:0}
html,body{width:1069px;height:1200px;overflow:hidden}
body{font-family:"Roboto",Arial,sans-serif;background:var(--page);position:relative;color:var(--body)}

/* header */
.topbar{position:absolute;left:0;top:0;width:1019px;height:59px;background:linear-gradient(#fdfdfd,#f1f1f1);border-bottom:1px solid #dcdcdc}
.brand{position:absolute;left:20px;top:17px;font-size:20px;font-weight:300;color:#9a9a9a}
.search{position:absolute;left:265px;top:14px;width:395px;height:32px;border:1px solid #cfcfcf;border-radius:16px;background:var(--white);overflow:hidden;display:flex;align-items:center}
.search svg{margin-left:14px}
.search-query{flex:1;font-size:12px;font-style:italic;color:#444;margin-left:8px}
.search-btn{height:100%;width:59px;font-size:10px;display:flex;align-items:center;justify-content:center;border-left:1px solid #cfcfcf}
.search-btn.save{background:var(--soft-blue);color:var(--navy-text);font-weight:500}
.search-btn.clear{background:#f1f1f1;color:#888}
.mainnav{position:absolute;left:676px;top:0;height:59px;display:flex}
.mainnav a{display:flex;align-items:center;gap:6px;padding:0 14px;font-size:12.5px;font-weight:500;color:var(--navy-text);text-decoration:none;border-left:1px solid #dcdcdc;margin:12px 0;height:35px}

/* side rail */
.rail{position:absolute;left:1019px;top:0;width:50px;height:1200px;background:var(--rail)}
.rail-btn{height:45px;background:var(--navy);border-bottom:1px solid #26306a;display:flex;align-items:center;justify-content:center}

/* title band */
.page-title{position:absolute;left:0;top:59px;width:1019px;height:122px;background:var(--white);display:flex;align-items:center;justify-content:center;gap:10px;font-family:"Roboto Slab",Georgia,serif;font-weight:300;font-size:33px;color:var(--navy-text)}
.crumbs{position:absolute;left:0;top:181px;width:1019px;height:45px;background:var(--navy);display:flex;align-items:center;padding-left:40px;font-size:12.5px;font-weight:500;color:var(--white)}
.crumbs a{color:var(--cyan);text-decoration:none}
.crumbs span.sep{margin:0 7px;color:var(--white)}
.create{position:absolute;right:40px;top:8px;height:29px;padding:0 11px;background:var(--cyan-btn);border-radius:3px;display:flex;align-items:center;gap:5px;font-size:11.5px;font-weight:700;color:var(--white)}

/* threads */
.avatar{position:absolute;width:100px;height:100px;border-radius:50%;border:1px solid #bbb;background:radial-gradient(circle at 50% 40%,#c9b3a3,#8a7b70 70%,#d9d9d9)}
.author{position:absolute;font-size:10.5px;font-weight:500;font-style:italic;color:var(--navy-text);text-decoration:underline}
.stamp{position:absolute;font-size:9px;font-style:italic;color:#777}
.card{position:absolute;width:823px;height:173px;background:var(--white);border:1px solid var(--line)}
.card::before{content:"";position:absolute;top:38px;width:12px;height:12px;background:var(--white);border:1px solid var(--line);transform:rotate(45deg)}
.card.left-tail::before{left:-7px;border-right:none;border-top:none}
.card.right-tail::before{right:-7px;border-left:none;border-bottom:none}
.card h2{position:absolute;left:20px;top:17px;font-size:20px;font-weight:500;color:var(--cyan)}
.card p{position:absolute;left:20px;top:45px;width:792px;font-size:12.7px;line-height:21px;color:var(--body)}
.more{color:var(--cyan);font-style:italic;font-size:10.5px;text-decoration:underline}
.actions{position:absolute;right:-1px;bottom:-1px;display:flex;height:29px}
.actions div{display:flex;align-items:center;justify-content:center;gap:5px;border:1px solid var(--line);margin-left:-1px;font-size:9.5px}
.stat{background:var(--stat);color:var(--muted);width:99px}
.act{background:var(--soft-blue);color:var(--navy-text);font-weight:500}

.reply-box{position:absolute;left:272px;top:431px;width:707px;height:128px;background:var(--soft-blue);border:1px solid var(--navy)}
.reply-box::before{content:"";position:absolute;left:-7px;top:20px;width:12px;height:12px;background:var(--soft-blue);border-left:1px solid var(--navy);border-bottom:1px solid var(--navy);transform:rotate(45deg)}
.reply-box .hint{position:absolute;left:20px;top:18px;font-size:12px;font-style:italic;color:#666}
.reply-send{position:absolute;right:-1px;bottom:-1px;width:120px;height:28px;background:var(--navy);color:var(--white);font-size:9.5px;font-weight:500;display:flex;align-items:center;justify-content:center;gap:6px}
</style>
</head>
<body>

<header class="topbar">
  <div class="brand">Company Name</div>
  <div class="search">
    <svg width="15" height="15" viewBox="0 0 16 16"><circle cx="6.5" cy="6.5" r="5" fill="none" stroke="#aaa" stroke-width="1.6"/><line x1="10" y1="10" x2="15" y2="15" stroke="#aaa" stroke-width="1.8"/></svg>
    <span class="search-query">#Talvenix #Orbrelle</span>
    <span class="search-btn save">SAVE</span>
    <span class="search-btn clear">CLEAR</span>
  </div>
  <nav class="mainnav">
    <a href="#"><svg width="20" height="17" viewBox="0 0 20 17"><rect x="1" y="1" width="12" height="8" fill="none" stroke="#0b1446" stroke-width="1.8"/><path d="M6 11h13V4h-4" fill="none" stroke="#0b1446" stroke-width="1.8"/><path d="M14 11v4l-3-4" fill="#0b1446"/></svg>PUBLIC</a>
    <a href="#"><svg width="17" height="17" viewBox="0 0 17 17"><circle cx="8.5" cy="8.5" r="6.5" fill="none" stroke="#0b1446" stroke-width="2" stroke-dasharray="8 2.5"/></svg>FOLLOWING</a>
    <a href="#"><svg width="14" height="17" viewBox="0 0 14 17"><path d="M3.5 8V5a3.5 3.5 0 017 0v3" fill="none" stroke="#0b1446" stroke-width="1.6"/><rect x="1.5" y="8" width="11" height="8" fill="none" stroke="#0b1446" stroke-width="1.6"/></svg>CONTACTS</a>
  </nav>
</header>

<aside class="rail">
  <div class="rail-btn"><svg width="16" height="18" viewBox="0 0 16 18"><circle cx="8" cy="5" r="4" fill="#fff"/><path d="M1 18c0-5 3-7 7-7s7 2 7 7z" fill="#fff"/></svg></div>
  <div class="rail-btn"><svg width="24" height="18" viewBox="0 0 24 18"><circle cx="12" cy="5" r="3.5" fill="#fff"/><circle cx="5" cy="7" r="2.7" fill="#fff"/><circle cx="19" cy="7" r="2.7" fill="#fff"/><path d="M6 17c0-5 3-7 6-7s6 2 6 7zM0 16c0-4 2-5 5-5 1 0 2 .5 2 .5L5 16zM24 16c0-4-2-5-5-5-1 0-2 .5-2 .5l2 4.5z" fill="#fff"/></svg></div>
  <div class="rail-btn"><svg width="18" height="18" viewBox="0 0 18 18"><path d="M1 1h16l-6 8v8l-4-2V9z" fill="#fff"/></svg></div>
  <div class="rail-btn"><svg width="20" height="20" viewBox="0 0 20 20"><circle cx="10" cy="10" r="8.5" fill="none" stroke="#fff" stroke-width="2"/><path d="M3 7c4 0 6 3 5 6M10 2c2 3 6 4 8 4M12 18c0-4 3-6 6-6" fill="none" stroke="#fff" stroke-width="2"/></svg></div>
  <div class="rail-btn"><svg width="20" height="18" viewBox="0 0 20 18"><path d="M2 6h4l10-5v16L6 12H2z" fill="#fff"/><path d="M5 12l2 5h2l-1-5" fill="#fff"/></svg></div>
  <div class="rail-btn"><svg width="20" height="20" viewBox="0 0 20 20"><circle cx="10" cy="10" r="9" fill="#fff"/><path d="M11 5l-5 5 5 5M6 10h9" fill="none" stroke="#06103f" stroke-width="2.4"/></svg></div>
</aside>

<section class="page-title">
  <svg width="40" height="36" viewBox="0 0 40 36"><rect x="2" y="2" width="24" height="16" fill="none" stroke="#0b1446" stroke-width="3"/><path d="M12 22h26V8h-8" fill="none" stroke="#0b1446" stroke-width="3"/><path d="M28 22v10l-7-10" fill="#0b1446"/><path d="M8 18v6l5-6" fill="#0b1446"/></svg>
  PUBLIC: TALVENIX
</section>

<nav class="crumbs">
  <a href="#">HOME</a><span class="sep">&gt;</span><a href="#">CONVERSATIONS</a><span class="sep">&gt;</span><a href="#">PUBLIC</a><span class="sep">&gt;</span>#TALVENIX#ORBRELLE
  <div class="create"><svg width="12" height="12" viewBox="0 0 12 12"><path d="M6 0v12M0 6h12" stroke="#fff" stroke-width="3"/></svg>CREATE THREAD</div>
</nav>

<!-- thread 1 -->
<div class="avatar" style="left:40px;top:247px" role="img" aria-label="Portrait photo of Martin Keble"></div>
<a class="author" style="left:40px;top:360px">Martin Keble</a>
<span class="stamp" style="left:40px;top:379px">01/01/2014 - 15:32</span>
<article class="card left-tail" style="left:156px;top:247px">
  <h2>Lorem Ipsum Subject</h2>
  <p>Lorem ipsum dolor sit amet, consectetur adipiscing elit. Pellentesque euismod ac leo a faucibus. Vivamus dui enim, vehicula hendrerit eros ut, laoreet viverra lacus. Duis feugiat augue dolor, eget porttitor velit ullamcorper non. Donec quis felis dapibus, suscipit velit sit amet, facilisis metus. Cras at placerat nulla. Cras elementum tempor enim vel porta. Integer arcu augue, tempus ut fringilla vel, porttitor nec massa. Quisque tincidunt felis et tellus vestibulum, in dignissim diam aliquam. Nunc porta ullamcorper augue eu aliquam... <span class="more">&gt; READ MORE</span></p>
  <div class="actions">
    <div class="stat">💬 12 REPLIES</div><div class="stat">◉ 250 VIWES</div>
    <div class="act" style="width:76px">➦ REPLY</div><div class="act" style="width:74px">⋖ SHARE</div><div class="act" style="width:99px">★ FAVOURITE</div>
  </div>
</article>

<div class="avatar" style="left:156px;top:431px" role="img" aria-label="Portrait photo of the signed-in user"></div>
<span class="author" style="left:156px;top:545px;text-decoration:none">You: Peter Vandel</span>
<div class="reply-box">
  <span class="hint">Type your reply!</span>
  <div class="reply-send">➦ LEAVE A REPLY</div>
</div>

<!-- thread 2 -->
<article class="card right-tail" style="left:40px;top:618px">
  <h2>Quisque Convallis Euismod Ante Subject</h2>
  <p>Quisque convallis euismod ante, sit amet fringilla magna dapibus et. Morbi tincidunt libero ac suscipit lacinia. Ut tristique justo eget odio viverra elementum. Praesent lectus orci, laoreet sed elementum eu, dictum vel lectus. Integer ultricies odio vitae dolor fringilla, ut dictum nisl sollicitudin. Ut varius lorem nec leo sodales, vel laoreet ipsum suscipit. Proin porta vel sem non elementum. Nunc leo metus, feugiat sed consequat quis, consequat vitae felis. Phas ellus posuere magna eleme ntum ipsum sodales, et congue odio pretium... <span class="more">&gt; READ MORE</span></p>
  <div class="actions">
    <div class="stat">💬 17 REPLIES</div><div class="stat">◉ 225 VIWES</div>
    <div class="act" style="width:76px">➦ REPLY</div><div class="act" style="width:74px">⋖ SHARE</div><div class="act" style="width:99px">★ FAVOURITE</div>
  </div>
</article>
<div class="avatar" style="left:878px;top:618px" role="img" aria-label="Portrait photo of Nadia Schoer"></div>
<a class="author" style="left:878px;top:729px">Nadia Schoer</a>
<span class="stamp" style="left:878px;top:748px">01/01/2014 - 05:30</span>

<!-- thread 3 -->
<div class="avatar" style="left:40px;top:812px" role="img" aria-label="Portrait photo of Robert Halme"></div>
<a class="author" style="left:40px;top:923px">Robert Halme</a>
<span class="stamp" style="left:40px;top:942px">12/28/2013 - 21:06</span>
<article class="card left-tail" style="left:156px;top:812px">
  <h2>In At Mi Risus Subject</h2>
  <p>In at mi risus. Integer tempor iaculis nisl eget tempor. Nam consectetur neque justo. Vivamus molestie risus a eleifend lobortis. Pellentesque interdum interdum purus, ac fringilla mi mattis ut. Etiam dignissim ut odio sed adipiscing. Aenean vel quam eget velit congue aliquam eget ac orci. Morbi aliquet, elit at varius dictum, erat nibh congue lorem, at ultricies dolor magna eu justo. Aenean faucibus orci et risus elementum gravida sodales in mauris. Cras auctor at sem scelerisque mollis. Mauris vel volutpat metus. Curabitur non... <span class="more">&gt; READ MORE</span></p>
  <div class="actions">
    <div class="stat">💬 34 REPLIES</div><div class="stat">◉ 316 VIWES</div>
    <div class="act" style="width:76px">➦ REPLY</div><div class="act" style="width:74px">⋖ SHARE</div><div class="act" style="width:99px">★ FAVOURITE</div>
  </div>
</article>

<!-- thread 4 -->
<article class="card right-tail" style="left:40px;top:1006px">
  <h2>Cras Iaculis Uurna Id Hendrerit Pretium Subject</h2>
  <p>Cras iaculis, urna id hendrerit pretium, nisi augue pellentesque odio, vitae pellentesque ligula orci auctor odio. Aenean varius tincidunt suscipit. Nunc faucibus aliquam justo, et adipiscing enim feugiat in. Nullam auctor, sapien ac bibendum imperdiet, augue sapien placerat arcu, non gravida nibh dolor sit amet urna. Donec vulputate erat neque, eget aliquam nunc sagittis ut. Nam vestibulum libero ultrices metus elementum condimentum sed nec quam. Maecenas fermentum volutpat tincidunt. Nam facilisis tortor eu tortor moles... <span class="more">&gt; READ MORE</span></p>
  <div class="actions">
    <div class="stat">💬 23 REPLIES</div><div class="stat">◉ 169 VIWES</div>
    <div class="act" style="width:76px">➦ REPLY</div><div class="act" style="width:74px">⋖ SHARE</div><div class="act" style="width:99px">★ FAVOURITE</div>
  </div>
</article>
<div class="avatar" style="left:878px;top:1006px" role="img" aria-label="Portrait photo of James R. Welden"></div>
<a class="author" style="left:878px;top:1117px">James R. Welden</a>
<span class="stamp" style="left:878px;top:1136px">12/22/2013 - 03:05</span>

</body>
</html>
```